Business Card Design

Velvet Pixel Promotions

An online marketing consulting & strategy business for the cosmetic niche

We specialise in Increasing Leads, Conversions & Content Marketing

I am looking for a very clean, BOLD business card that is simple & effective

Target Market(s)

cosmetic surgeons & cosmetic clinics

Industry/Entity Type

Marketing

Contact Information for Business Card

Darren Okoye
Online Marketing Strategist

Darren@VelvetPixelPromotions.example
0491 268 517

LinkedIn: in/darrenokoye

```html
<!DOCTYPE html>
<html lang="en">
<head>
<meta charset="utf-8">
<title>Velvet Pixel Promotions – Business Card</title>
<link rel="stylesheet" href="https://fonts.googleapis.com/css2?family=Varela+Round&display=swap">
<style>
  :root {
    --stage: #2b2b2b;
    --card-dark: #121212;
    --card-light: #f4f4f4;
    --ink: #111111;
    --white: #f2f2f2;
    --teal: #1fb3c8;
    --teal-muted: #3f8f86;
    --font: "Varela Round", sans-serif;
  }
  * { box-sizing: border-box; margin: 0; padding: 0; }
  html, body {
    width: 1200px; height: 900px; overflow: hidden;
    background: var(--stage);
    font-family: var(--font);
  }
  .stage {
    width: 1200px; height: 900px;
    display: flex; flex-direction: column;
    align-items: center; justify-content: center; gap: 50px;
  }
  .card {
    width: 600px; height: 343px;
    border-radius: 4px;
    overflow: hidden;
    box-shadow: 0 10px 30px rgba(0,0,0,.45);
  }

  /* Front */
  .card-front {
    background: var(--card-dark);
    display: flex; align-items: center; justify-content: center; gap: 22px;
  }
  .brand-dot {
    width: 92px; height: 92px; border-radius: 50%;
    background: var(--teal);
    flex: none;
  }
  .brand-name {
    color: var(--white);
    font-size: 38px; line-height: 1.02;
    text-transform: uppercase;
    letter-spacing: 3px;
  }
  .brand-name span { display: block; }

  /* Back */
  .card-back { display: flex; }
  .back-strip {
    width: 190px; background: var(--card-dark);
    display: flex; flex-direction: column; align-items: center; justify-content: center; gap: 14px;
  }
  .strip-dot {
    width: 96px; height: 96px; border-radius: 50%;
    background: var(--teal-muted);
  }
  .strip-name {
    color: var(--teal-muted);
    font-size: 11px; letter-spacing: 1.5px; text-transform: uppercase;
    text-align: center; line-height: 1.3;
  }
  .back-details {
    flex: 1; background: var(--card-light);
    color: var(--ink);
    padding: 58px 34px 34px 20px;
    display: flex; flex-direction: column; align-items: flex-end; text-align: right;
  }
  .person-name { font-size: 30px; font-weight: 700; line-height: 1.05; }
  .person-title { font-size: 15px; font-weight: 700; margin-top: 2px; }
  .contact-list { list-style: none; margin-top: 34px; font-size: 13px; line-height: 1.6; }
  .contact-list li { display: flex; align-items: center; justify-content: flex-end; gap: 6px; }
  .contact-square { width: 14px; height: 14px; background: var(--ink); border-radius: 2px; }
  .contact-email { margin-top: auto; font-size: 14px; }
</style>
</head>
<body>
<main class="stage">
  <section class="card card-front" aria-label="Card front">
    <div class="brand-dot"></div>
    <h1 class="brand-name"><span>Velvet</span><span>Pixel</span><span>Promotions</span></h1>
  </section>

  <section class="card card-back" aria-label="Card back">
    <div class="back-strip">
      <div class="strip-dot"></div>
      <p class="strip-name">Velvet<br>Pixel<br>Promotions</p>
    </div>
    <div class="back-details">
      <h2 class="person-name">Darren Okoye</h2>
      <p class="person-title">Online Marketing Strategist</p>
      <ul class="contact-list">
        <li>0491 268 517</li>
        <li><span class="contact-square"></span>in/darrenokoye</li>
      </ul>
      <p class="contact-email">Darren@VelvetPixelPromotions.example</p>
    </div>
  </section>
</main>
</body>
</html>
```